A Modern & Sleek "Coming Soon" Page for an A.I Recruiting App

For the “Coming Soon” website, a simple background with no people in it. I've attached an A.I image of what the page should generally look like.

- A single mobile phone as the main focus where the user actually clicks on the, “notify me” button (after entering their email address).
- In the background where the pillars/columns are seen in the example, should be subtle pad locks that are in their opened position with a key inside the lock. I've attached images to try to illustrate this idea, but they are far away in style from what I'm looking for.

SLOGAN: Unlocking the power of meaningful connections
LOGO/TITLE: Should be the name as shown in image with only the name "KelpLoop" on it
COLORS: Purplish/blue hues. Should not be too feminine
NOTE: The user should only click once when signing up/entering their email.

Product: A recruiting platform that matches employers/employees with A.I. and prioritizing cultural fit/values system before skills. The industry we are tackling first is the caregiving industry (nannies, tutors, elderly). All users will be background screened and that info lives on the blockchain. All users will have the option to review and be reviewed/rated.

```html
<!DOCTYPE html>
<html lang="en">
<head>
<meta charset="UTF-8">
<title>KelpLoop — Coming Soon</title>
<link href="https://fonts.googleapis.com/css2?family=Montserrat:wght@300;400;500;600;700&display=swap" rel="stylesheet">
<style>
  :root {
    --bg-top: #3a0866;
    --bg-mid: #44098a;
    --bg-right: #520fae;
    --footer-bg: #3e0c78;
    --white: #ffffff;
    --ink: #2a0a55;
    --rule: rgba(255,255,255,0.55);
    --footer-text: #c9b3ee;
    --art-mid: #5a1a8c;
    --device-screen: #4a0fa0;
    --device-edge: #e9e9ee;
    --device-notch: #111014;
  }
  * { margin: 0; padding: 0; box-sizing: border-box; }
  html, body { width: 1200px; height: 759px; overflow: hidden; }
  body {
    font-family: "Montserrat", sans-serif;
    color: var(--white);
    background: linear-gradient(125deg, var(--bg-top) 0%, var(--bg-mid) 50%, var(--bg-right) 100%);
    position: relative;
  }
  .site-header { position: absolute; top: 0; left: 0; width: 1200px; height: 76px; }
  .brand {
    position: absolute; left: 137px; top: 20px;
    font-weight: 300; font-size: 33px; letter-spacing: 3px; line-height: 36px;
  }
  .menu-toggle {
    position: absolute; left: 961px; top: 28px;
    display: flex; align-items: center; gap: 24px;
    font-weight: 600; font-size: 15px; letter-spacing: 0.5px;
  }
  .menu-toggle .bars { display: flex; flex-direction: column; gap: 6px; }
  .menu-toggle .bars span { display: block; width: 33px; height: 1.5px; background: var(--white); }

  .lock-art {
    position: absolute; left: 94px; top: 56px; width: 612px; height: 570px;
    border-radius: 200px 60px 40px 40px;
    background: radial-gradient(ellipse at 50% 55%, var(--art-mid) 0%, rgba(60,10,100,0.35) 55%, rgba(60,10,100,0) 75%);
    opacity: 0.7;
  }

  .device {
    position: absolute; left: 244px; top: 134px; width: 204px; height: 525px;
    border-radius: 30px;
    border: 5px solid var(--device-edge);
    background: linear-gradient(180deg, #3a0a88 0%, var(--device-screen) 60%, #5212b0 100%);
    box-shadow: 0 10px 30px rgba(0,0,0,0.35);
    overflow: hidden;
  }
  .device-notch {
    position: absolute; left: 45px; top: -2px; width: 104px; height: 22px;
    background: var(--device-notch); border-radius: 0 0 14px 14px;
  }
  .device-screen {
    position: absolute; left: 0; top: 170px; width: 194px;
    text-align: center;
    transform: rotate(-3deg);
  }
  .screen-brand {
    font-weight: 300; font-size: 21px; letter-spacing: 1.5px; line-height: 24px;
  }
  .screen-tagline {
    margin-top: 22px;
    font-weight: 400; font-size: 12.5px; line-height: 15px;
  }
  .notify-button {
    display: inline-flex; align-items: center; justify-content: center;
    margin-top: 26px; width: 92px; height: 36px;
    border: none; border-radius: 18px;
    background: var(--white); color: var(--ink);
    font-family: "Montserrat", sans-serif; font-weight: 700; font-size: 11px; letter-spacing: 0.3px;
  }

  .hero { position: absolute; left: 619px; top: 280px; width: 440px; }
  .hero-title {
    font-weight: 500; font-size: 70px; line-height: 70px; letter-spacing: 1px; white-space: nowrap;
  }
  .hero-rule { margin: 14px 0 0 11px; width: 410px; height: 1px; background: var(--rule); }
  .hero-tagline {
    margin: 14px 0 0 9px;
    font-weight: 500; font-size: 26px; line-height: 32px;
  }
  .signup-button {
    display: inline-flex; align-items: center; justify-content: center;
    margin: 20px 0 0 12px; width: 130px; height: 45px;
    border: 2px solid var(--white); border-radius: 23px;
    font-weight: 600; font-size: 14px; letter-spacing: 0.5px; color: var(--white);
    background: transparent; font-family: "Montserrat", sans-serif;
  }

  .site-footer {
    position: absolute; left: 0; top: 705px; width: 1200px; height: 54px;
    background: var(--footer-bg);
  }
  .copyright {
    position: absolute; left: 0; width: 1264px; top: 19px; text-align: center;
    font-size: 11.5px; color: var(--footer-text);
  }
  .social-links { position: absolute; left: 994px; top: 14px; display: flex; gap: 4px; }
  .social-links span {
    display: block; width: 26px; height: 26px; border-radius: 50%;
    border: 1.5px solid var(--white);
  }
</style>
</head>
<body>
  <header class="site-header">
    <div class="brand">KELPLOOP</div>
    <div class="menu-toggle">MENU <div class="bars"><span></span><span></span><span></span></div></div>
  </header>

  <div class="lock-art" role="img" aria-label="Subtle open padlock with a key in the background"></div>

  <div class="device">
    <div class="device-notch"></div>
    <div class="device-screen">
      <div class="screen-brand">KELPLOOP</div>
      <p class="screen-tagline">Unlocking the Power of<br>Meaningful<br>Connections.</p>
      <button class="notify-button">NOTIFY ME</button>
    </div>
  </div>

  <main class="hero">
    <h1 class="hero-title">KELP LOOP</h1>
    <div class="hero-rule"></div>
    <p class="hero-tagline">Unlocking the Power of<br>Meaningful Connections.</p>
    <button class="signup-button">SIGN UP</button>
  </main>

  <footer class="site-footer">
    <p class="copyright">© 2024 Company Name | All Rights Reserved</p>
    <div class="social-links">
      <span aria-label="Social link"></span>
      <span aria-label="Social link"></span>
      <span aria-label="Social link"></span>
    </div>
  </footer>
</body>
</html>
```